Harbor Learning Center Posters Showing Building Blocks

We need poster designs for a School in Arizona for kids with Autism. There will be 4 such posters needed which highlight our schools building blocks. Requirements for all 4 posters are as followed: 1) We need the Harbor Learning Center Logo on each poster. I have included attachment. 2) The posters need the following titles: Building Block #1 (for the first poster), Building Block #2 for the 2nd poster, Building Block #3 for the 3rd poster, and Building Block #4 for the forth poster. 3) The main text and focus of the posters will be the following key words: For the first poster the words "Kids first in every decision". The words for the second poster are: "Students are friends with each other, and welcome new students with open arms." The words for the 3rd poster are: "The school is quiet, and students are working hard to do their best." The words for the 4th poster are: "Parents see amazing improvement in their child." 4) We would love to use some of the kids art from our schools if possible. Use your expertise to decide. I will send these out as well. 5) Try and design the posters around the key words from each poster 6) I am sure if landscape or portrait would be best so I will let the experts decide. All 4 posters need to be the same layout once decided.

Target Market(s)

These posters are for the school only. Prospective students/parents will see these posters so they will be used for Marketing from that perspective. We may put out into local community in future.

Industry/Entity Type

School

Font styles to use
Serif

Requirements
Must have
• 1) Logo (Harbor Learning Center for Growth and Discovery)
• 2) Title: as described in write up
• 3) Key words: as described in write up
Nice to have
• Kids art from school. Note: This is the first time that I have been on this site so I may have made a mistake by putting 4 posters on one project. I am assuming that I would need to pay more to have 4 posters so let me know if I need to modify the project in any way?

```html
<!DOCTYPE html>
<html lang="en">
<head>
<meta charset="utf-8">
<title>Building Block #3 – Harbor Learning Center</title>
<link rel="stylesheet" href="https://fonts.googleapis.com/css2?family=Kalam:wght@700&family=Tinos:wght@400;700&display=swap">
<style>
  :root {
    --backdrop: #e9e6e1;
    --paper: #f7f7f5;
    --board: #2c2e30;
    --board-edge: #1f2122;
    --chalk: #f2f2f0;
    --frame-wood: #5a3a26;
    --frame-wood-top: #654330;
    --frame-wood-dark: #3d2517;
    --art-orange: #e8652a;
    --art-green: #2f5a3a;
    --art-blue: #1e3f7a;
    --accent-red: #c8202a;
    --mark-tone: #8a8d90;
  }

  * { box-sizing: border-box; margin: 0; padding: 0; }

  html, body {
    width: 923px;
    height: 1200px;
    overflow: hidden;
    background: var(--backdrop);
  }

  .poster {
    position: absolute;
    left: 49px;
    top: 25px;
    width: 825px;
    height: 1150px;
    padding: 23px;
    background: var(--paper);
    box-shadow: 0 6px 18px rgba(0, 0, 0, 0.18);
  }

  .board {
    position: relative;
    width: 100%;
    height: 100%;
    background:
      radial-gradient(ellipse at 50% 35%, #3a3c3e 0%, var(--board) 55%, var(--board-edge) 100%);
  }

  .block-title {
    position: absolute;
    top: 58px;
    left: 0;
    right: 0;
    text-align: center;
    font-family: "Tinos", "Times New Roman", serif;
    font-weight: 700;
    font-size: 17px;
    letter-spacing: 0.5px;
    color: var(--chalk);
  }

  .art-frame {
    position: absolute;
    left: 76px;
    top: 111px;
    width: 640px;
    height: 432px;
    border: 25px solid var(--frame-wood);
    border-top-color: var(--frame-wood-top);
    border-bottom-color: var(--frame-wood-dark);
    box-shadow: 0 10px 18px rgba(0, 0, 0, 0.55), inset 0 0 0 2px #1c120b;
  }

  .student-art {
    width: 100%;
    height: 100%;
    background:
      linear-gradient(175deg,
        var(--art-green) 0%,
        var(--art-orange) 22%,
        #d9541f 45%,
        var(--art-blue) 62%,
        var(--art-green) 80%,
        #22402e 100%);
  }

  .key-words {
    position: absolute;
    top: 600px;
    left: 20px;
    right: 20px;
    text-align: center;
    font-family: "Kalam", "Comic Sans MS", cursive;
    font-weight: 700;
    font-size: 43px;
    line-height: 57px;
    text-transform: uppercase;
    color: var(--chalk);
  }

  .school-mark {
    position: absolute;
    left: 160px;
    top: 866px;
    width: 66px;
    height: 66px;
    background: var(--mark-tone);
  }

  .school-name {
    position: absolute;
    left: 240px;
    top: 938px;
    font-family: "Tinos", "Times New Roman", serif;
    font-weight: 400;
    font-size: 25px;
    line-height: 38px;
    color: var(--chalk);
  }

  .school-name .name-line {
    display: block;
    border-bottom: 3px solid var(--accent-red);
    padding-bottom: 2px;
    margin-bottom: 2px;
  }
</style>
</head>
<body>
  <main class="poster">
    <section class="board">
      <h1 class="block-title">BUILDING BLOCK #3</h1>

      <figure class="art-frame">
        <div class="student-art" role="img" aria-label="Framed student painting: bold orange, green and blue brushstrokes with dark dabs of paint"></div>
      </figure>

      <p class="key-words">"The school is quiet, and<br>students are working hard<br>to do their best."</p>

      <div class="school-mark" aria-hidden="true"></div>
      <p class="school-name"><span class="name-line">HARBOR LEARNING CENTER</span>for Growth and Discovery</p>
    </section>
  </main>
</body>
</html>
```